Signage for shopfront window (4 panels). Allied Health

We are a health practice that delivers speech pathology, occupational therapy and psychology services to children and adults.

Shop front has 4 glass panels (floor to ceiling height. 2nd panel is an automatic sliding door that moves to the right when it opens). See Picture.

Design needs to include these elements:
1. QLRT logo (provided)
2. Vitacove logo (provided)
3. clinic logo (provided)
4. Our 3 services: Speech Pathology, Occupational Therapy, Psychology.
7. Happy to consider graphics/photos on the design that depicts adult and child, but not necessary (maybe an option that shows a graphic and one that doesn’t?)
8. Background to the entire design (ie, all the negative space) will be frosted glass (not a white background)
9. we want an inviting and bright shopfront, without looking too childlike or too clinical.
10. look at our website for inspiration of our look and feel. Please also look at the look and feel of our logo for inspiration.
11. other information to go on front: “Ph: 6203 4418” “brightpathwell.com.au”

Final design MUST be a high resolution PDF so the printers can use it to adjust any measurements for best quality printing and installation on the shopfront glass windows.

```html
<!DOCTYPE html>
<html lang="en">
<head>
<meta charset="utf-8">
<title>Bright Path – Shopfront Window Signage</title>
<link rel="stylesheet" href="https://fonts.googleapis.com/css2?family=Bebas+Neue&family=Montserrat:wght@700&family=Oswald:wght@500&display=swap">
<style>
  :root {
    --backdrop: #d0d0d0;
    --glass: #ffffff;
    --teal: #38a7b1;
    --lime: #a9cd52;
    --leaf: #7cc576;
    --ink: #1e1e1e;
    --chip: #e6e6e6;
    --vita-green: #1a9a6c;
  }
  * { box-sizing: border-box; margin: 0; padding: 0; }
  html, body { width: 857px; height: 1200px; overflow: hidden; background: var(--backdrop); }
  .canvas { position: relative; width: 857px; height: 1200px; }
  .shopfront { position: absolute; left: 27px; top: 373px; width: 803px; height: 454px; }
  .shopfront-art { position: absolute; inset: 0; width: 803px; height: 454px; }
  .panel { position: absolute; top: 0; height: 454px; }
  .panel--brand { left: 0; width: 191px; }
  .panel--speech { left: 201px; width: 178px; }
  .panel--ot { left: 389px; width: 212px; }
  .panel--psych { left: 611px; width: 192px; }

  .service-title {
    position: absolute; top: 38px; left: 0; right: 0;
    font-family: "Bebas Neue", "Oswald", sans-serif; font-weight: 400;
    font-size: 41px; line-height: 36px; color: var(--teal);
    text-align: center; letter-spacing: 0.2px;
  }

  .brand-name {
    position: absolute; left: 28px; top: 62px;
    display: flex; align-items: center; gap: 8px;
    font-family: "Montserrat", sans-serif; font-weight: 700;
    font-size: 21px; color: var(--teal); line-height: 1;
  }
  .brand-name .brand-mark { width: 16px; height: 16px; background: var(--lime); }

  .contact { position: absolute; left: 18px; top: 210px; }
  .contact-row { display: flex; align-items: center; gap: 6px; height: 18px; }
  .contact-icon { width: 9px; height: 9px; flex: none; }
  .contact-phone { font-family: "Montserrat", sans-serif; font-weight: 700; font-size: 21px; color: var(--ink); height: 26px; }
  .contact-phone .contact-icon { width: 10px; height: 10px; }
  .contact-line { font-family: "Oswald", sans-serif; font-weight: 500; font-size: 10.5px; color: var(--ink); letter-spacing: -0.1px; }

  .provider-badge {
    position: absolute; left: 16px; top: 294px; width: 148px; height: 67px;
    background: var(--chip); border-radius: 4px;
  }

  .partner-name {
    position: absolute; left: 22px; top: 382px; width: 150px; height: 34px;
    display: flex; align-items: center; gap: 8px;
    font-family: "Montserrat", sans-serif; font-weight: 700; font-size: 21px; color: var(--vita-green);
  }
  .partner-name .partner-mark { width: 12px; height: 12px; background: var(--vita-green); }
</style>
</head>
<body>
<main class="canvas">
  <section class="shopfront" aria-label="Four-panel shopfront window signage">
    <svg class="shopfront-art" viewBox="0 0 803 454" xmlns="http://www.w3.org/2000/svg">
      <defs>
        <clipPath id="glass-panels">
          <rect x="0" y="0" width="191" height="454"/>
          <rect x="201" y="0" width="178" height="454"/>
          <rect x="389" y="0" width="212" height="454"/>
          <rect x="611" y="0" width="192" height="454"/>
        </clipPath>
        <linearGradient id="ot-glow" x1="0" x2="1" y1="0" y2="0">
          <stop offset="0" stop-color="#ffffff" stop-opacity="0"/>
          <stop offset="1" stop-color="#e3ef9c"/>
        </linearGradient>
        <linearGradient id="psych-wash" x1="0" x2="1" y1="0" y2="0">
          <stop offset="0" stop-color="#cfe59a"/>
          <stop offset="0.35" stop-color="#8fd17a"/>
          <stop offset="0.7" stop-color="#46b08f"/>
          <stop offset="1" stop-color="#34a3a3"/>
        </linearGradient>
      </defs>
      <g clip-path="url(#glass-panels)">
        <rect x="0" y="0" width="803" height="454" fill="var(--glass)"/>
        <rect x="530" y="200" width="71" height="254" fill="url(#ot-glow)"/>
        <rect x="611" y="200" width="192" height="254" fill="url(#psych-wash)" role="img" aria-label="Soft green-to-teal wash with floating light bubbles"/>
        <path d="M0,178 Q400,120 803,196" fill="none" stroke="var(--lime)" stroke-width="6"/>
      </g>
    </svg>

    <div class="panel panel--brand">
      <div class="brand-name"><span class="brand-mark"></span>Bright Path</div>
      <div class="contact">
        <div class="contact-row contact-phone">
          <svg class="contact-icon" viewBox="0 0 10 10"><circle cx="5" cy="5" r="5" fill="var(--leaf)"/><path d="M3.2,2.6 L4.1,3.7 L3.7,4.3 C4.1,5.1 4.8,5.8 5.7,6.3 L6.3,5.9 L7.4,6.8 L6.8,7.6 C4.8,7.3 2.8,5.3 2.5,3.2 Z" fill="#fff"/></svg>
          <span>6203 4418</span>
        </div>
        <div class="contact-row contact-line">
          <svg class="contact-icon" viewBox="0 0 10 10"><circle cx="5" cy="5" r="5" fill="var(--leaf)"/><rect x="2.6" y="3.3" width="4.8" height="3.4" fill="none" stroke="#fff" stroke-width="0.7"/><path d="M2.6,3.3 L5,5.2 L7.4,3.3" fill="none" stroke="#fff" stroke-width="0.7"/></svg>
          <span>ADMIN@BRIGHTPATHWELL.COM.AU</span>
        </div>
        <div class="contact-row contact-line">
          <svg class="contact-icon" viewBox="0 0 10 10"><circle cx="5" cy="5" r="5" fill="var(--leaf)"/><circle cx="5" cy="5" r="2.6" fill="none" stroke="#fff" stroke-width="0.6"/><path d="M2.4,5 H7.6 M5,2.4 V7.6" stroke="#fff" stroke-width="0.6"/></svg>
          <span>WWW.BRIGHTPATHWELL.COM.AU</span>
        </div>
      </div>
      <div class="provider-badge" role="img" aria-label="QLRT registered provider badge"></div>
      <div class="partner-name"><span class="partner-mark"></span>Vitacove</div>
    </div>

    <div class="panel panel--speech"><h2 class="service-title">Speech<br>Pathology</h2></div>
    <div class="panel panel--ot"><h2 class="service-title">Occupational<br>Therapy</h2></div>
    <div class="panel panel--psych"><h2 class="service-title">Psychology</h2></div>
  </section>
</main>
</body>
</html>
```